Corvale Holdings Business Cards

Hello. I need business cards designed with our new logo. I'd like to see at least 3 different designs. At least one with a dark background, and at least one with a white background. Maybe one with gray or blue for the background. Play with gradient colors and maybe even insert a pic of a skyline in the background of one or more of them. Use your judgement. We will need 2 cards printed. They need to accommodate the employee name, title, company address, phone, email, and website. Thanks.

Target Market(s)

Wealthy mature investors.

Contact Information for Business Card

Single-sided, professional, clean design that incorporates our logo.

Font styles to use
Sans Serif

Requirements
Must have
• Our new logo needs to be featured on it. (See attached.)
• Employee Name (In all CAPS)
• Title
• Street Address, City, ST Zip Code
• Cell Phone #, Email Address, Website Address
Nice to have
• Design that blends well with our new logo and its colors, or a city scape or other graphic design that looks like an apartment complex in the background. Blues and grays are nice, but use your judgement.
Should not have
• Modern or oriental looking designs or bright colors.

```html
<!DOCTYPE html>
<html lang="en">
<head>
<meta charset="utf-8">
<title>Corvale Holdings – Business Card</title>
<link href="https://fonts.googleapis.com/css2?family=Lato:wght@400;700&display=swap" rel="stylesheet">
<style>
  :root {
    --page: #e8e8e8;
    --card: #505050;
    --accent: #22a3dc;
    --text: #ffffff;
    --text-soft: #f0f0f0;
  }
  * { box-sizing: border-box; margin: 0; padding: 0; }
  html, body {
    width: 1200px;
    height: 900px;
    overflow: hidden;
    background: var(--page);
    font-family: "Lato", sans-serif;
  }
  .business-card {
    position: absolute;
    left: 160px;
    top: 179px;
    width: 880px;
    height: 542px;
    background: var(--card);
    color: var(--text);
    overflow: hidden;
    box-shadow: 0 10px 30px rgba(0,0,0,0.18);
  }
  .accent-band {
    position: absolute;
    top: 0;
    right: 0;
    width: 178px;
    height: 100%;
    background: var(--accent);
  }
  .brand {
    position: absolute;
    left: 51px;
    top: 78px;
    display: flex;
    align-items: center;
    gap: 16px;
  }
  .brand-square {
    width: 44px;
    height: 44px;
    background: var(--accent);
  }
  .brand-name {
    font-weight: 700;
    font-size: 30px;
    letter-spacing: 1px;
    color: var(--text);
  }
  .person {
    position: absolute;
    left: 51px;
    top: 245px;
  }
  .person-name {
    font-weight: 700;
    font-size: 30px;
    letter-spacing: 0.5px;
    line-height: 1.1;
  }
  .person-title {
    font-size: 23px;
    color: var(--text-soft);
    margin-top: 2px;
  }
  .contact-list {
    position: absolute;
    left: 51px;
    top: 327px;
    list-style: none;
    font-size: 23px;
    line-height: 33px;
  }
  .contact-list li {
    display: flex;
    align-items: center;
    gap: 9px;
  }
  .contact-icon {
    width: 20px;
    height: 20px;
    fill: var(--text);
    flex: none;
  }
  .address {
    position: absolute;
    left: 54px;
    top: 434px;
    font-size: 23px;
    line-height: 33px;
    font-style: normal;
  }
</style>
</head>
<body>
  <section class="business-card">
    <div class="accent-band"></div>

    <div class="brand">
      <span class="brand-square"></span>
      <span class="brand-name">CORVALE HOLDINGS, LLC</span>
    </div>

    <div class="person">
      <div class="person-name">DANIEL WHITMORE</div>
      <div class="person-title">Managing Director</div>
    </div>

    <ul class="contact-list">
      <li>
        <svg class="contact-icon" viewBox="0 0 24 24" aria-hidden="true"><path d="M3 9c0-3 4-5 9-5s9 2 9 5v2h-5V9c-1-.6-2.5-1-4-1s-3 .4-4 1v2H3V9zm4 3h10l3 7H4l3-7zm5 1.5a2.5 2.5 0 1 0 0 5 2.5 2.5 0 0 0 0-5z"/></svg>
        <span>044-987 654 321</span>
      </li>
      <li>
        <svg class="contact-icon" viewBox="0 0 24 24" aria-hidden="true"><path d="M2 5h20v14H2V5zm2 2v.4l8 5.3 8-5.3V7H4zm0 2.8V17h16V9.8l-8 5.3-8-5.3z"/></svg>
        <span>info@corvaleholdings.com</span>
      </li>
      <li>
        <svg class="contact-icon" viewBox="0 0 24 24" aria-hidden="true"><circle cx="12" cy="12" r="10"/></svg>
        <span>www.corvaleholdings.com</span>
      </li>
    </ul>

    <address class="address">
      87, Linden Park Avenue,<br>
      60214, Northbridge
    </address>
  </section>
</body>
</html>
```